Tarvell homes and renovations business card design.

Would like some new card designs utilizing my new logo that look professional. I am open to different colors on the logo or utilize the same ones we have. I like the original concept but would like to see some fresh ideas and build on what we have already done.

Target Market(s)

Custom home building industry, Real estate sales, Renovation projects.

Industry/Entity Type

Home Builder

Contact Information for Business Card

Tarvell Homes and Renovations
2871 162nd Street
Elmvale, Northland
T0L3P0
Home : 403- 555-0187 Cell: 403- 555-0243

My info is : Gus Tarvell, President and CEO
email: tarvellhomes@quillmail.example
Website: tarvellhomes.example

Requirements
Must have
• Must Use my new logo design. I am open to different colors on the logo or utilize the same ones in the existing design. I can upload the original logo design if needed.

```html
<!DOCTYPE html>
<html lang="en">
<head>
<meta charset="utf-8">
<title>Tarvell Homes and Renovations – Business Cards</title>
<link rel="stylesheet" href="https://fonts.googleapis.com/css2?family=Montserrat:wght@400;600&display=swap">
<style>
  :root {
    --page: #e9e6e1;
    --card-black: #050505;
    --card-dark: #121110;
    --gold: #c8992b;
    --gold-band: #bf9128;
    --yellow: #fdd20c;
    --white: #f4f4f4;
  }
  * { box-sizing: border-box; margin: 0; padding: 0; }
  html, body { width: 1200px; height: 1200px; overflow: hidden; }
  body {
    background: var(--page);
    font-family: "Montserrat", Arial, sans-serif;
    position: relative;
  }
  .card {
    position: absolute;
    left: 180px;
    width: 840px;
    height: 480px;
    box-shadow: 0 14px 30px rgba(0,0,0,0.25);
    overflow: hidden;
  }
  .card--front { top: 90px; background: var(--card-black); }
  .card--back { top: 630px; background: var(--card-dark); }

  .wordmark {
    position: absolute;
    color: var(--gold);
    font-weight: 600;
    text-transform: uppercase;
    letter-spacing: 4px;
    line-height: 1.35;
    font-size: 30px;
    text-align: center;
  }
  .card--front .wordmark { left: 0; right: 0; top: 195px; }
  .card--back .wordmark { left: 150px; top: 110px; font-size: 28px; }

  .back-texture {
    position: absolute;
    inset: 0 0 74px 0;
    background: linear-gradient(160deg, #1a1916 0%, #0f0e0d 100%);
  }
  .divider {
    position: absolute;
    left: 60px;
    right: 40px;
    top: 300px;
    height: 2px;
    background: var(--yellow);
  }
  .phones {
    position: absolute;
    left: 60px;
    top: 318px;
    color: var(--white);
    font-size: 26px;
    line-height: 1.3;
  }
  .phones li, .address li { list-style: none; display: flex; align-items: center; gap: 10px; }
  .phones svg { width: 20px; height: 20px; fill: var(--yellow); }
  .address {
    position: absolute;
    right: 40px;
    top: 318px;
    color: var(--white);
    font-size: 22px;
    line-height: 1.35;
    text-align: right;
  }
  .address li { justify-content: flex-end; }
  .address svg { width: 18px; height: 18px; fill: var(--yellow); }
  .bands { position: absolute; left: 0; bottom: 0; width: 840px; height: 74px; }
</style>
</head>
<body>
  <section class="card card--front" aria-label="Card front">
    <p class="wordmark">Tarvell Homes<br>and Renovations</p>
  </section>

  <section class="card card--back" aria-label="Card back">
    <div class="back-texture" role="img" aria-label="Faint dark repeating name pattern background"></div>
    <p class="wordmark">Tarvell Homes<br>and Renovations</p>
    <div class="divider"></div>

    <ul class="phones">
      <li>
        <svg viewBox="0 0 20 20" aria-hidden="true"><rect x="5" y="1" width="10" height="18" rx="2"/><rect x="7" y="4" width="6" height="9" fill="#121110"/></svg>
        403- 555-0243
      </li>
      <li>
        <svg viewBox="0 0 20 20" aria-hidden="true"><path d="M2 8c0-3 4-5 8-5s8 2 8 5v2h-4V8H6v2H2z"/><rect x="4" y="11" width="12" height="7" rx="1"/></svg>
        403- 555-0187
      </li>
    </ul>

    <ul class="address">
      <li>2871 162nd Street
        <svg viewBox="0 0 20 20" aria-hidden="true"><path d="M10 2 1 10h3v8h5v-5h2v5h5v-8h3z"/></svg>
      </li>
      <li>Elmvale, Northland, T0L3P0</li>
    </ul>

    <svg class="bands" viewBox="0 0 840 74" aria-hidden="true">
      <polygon points="0,0 400,0 440,40 840,40 840,74 0,74" fill="var(--yellow)"/>
      <polygon points="400,0 840,0 840,40 440,40" fill="var(--gold-band)"/>
    </svg>
  </section>
</body>
</html>
```